Antigen Preservation Center

The company will provide a contract research services to stabilize various viruses, viral vectors, and vaccines. It may offer some licensing opportunities for stabilizing technologies. Main area of applications are pharmaceutical, therapeutic, and vaccination field. The company aspires to develop room temperature vaccines for global distribution beyond the current cold chain.
Updates

Target Market(s)

pharmaceutical, therapeutic and vaccination fields

Coding

Number of Pages Required

4 page

Requirements
Must have
• Incorporate a APC logo, attached at the bottom, on the Web page

```html
<!DOCTYPE html>
<html lang="en">
<head>
<meta charset="utf-8">
<title>Antigen Preservation Center</title>
<link rel="stylesheet" href="https://fonts.googleapis.com/css2?family=Exo+2:wght@300;400;600;700;800&family=Open+Sans:wght@400;600;700&display=swap">
<style>
:root{
  --teal:#14a58a;
  --teal-soft:#cfeee6;
  --orange:#d4922c;
  --gold:#f2b53b;
  --ink:#2d2d2d;
  --muted:#8a8a8a;
  --panel:#e8e9ea;
  --box:#eeebeb;
  --dark:#262626;
  --white:#ffffff;
}
*{margin:0;padding:0;box-sizing:border-box}
html,body{width:1200px;height:1200px;overflow:hidden;background:var(--white)}
body{font-family:'Open Sans',sans-serif;color:var(--ink)}
.stage{position:absolute;left:0;top:0;width:1500px;height:1500px;transform:scale(.8);transform-origin:0 0}
.page{position:absolute;left:432px;top:0;width:636px;height:1500px}
.abs{position:absolute}
.h{font-family:'Exo 2',sans-serif}

.topbar{left:0;top:0;width:636px;height:12px;background:var(--orange);color:var(--white);font-size:8px;text-align:right;padding-right:72px;line-height:12px}
.topbar b{font-weight:700}
.hero{left:0;top:12px;width:636px;height:313px;background:linear-gradient(180deg,#6fc8b2 0%,#9cc39a 45%,#c9a04a 80%,#d4962e 100%)}
.nav{left:0;top:12px;width:636px;height:30px;background:rgba(215,240,233,.85)}
.logo{left:70px;top:20px;display:flex;align-items:center;gap:6px;font-size:6px;letter-spacing:1.2px;color:var(--teal);font-weight:600;line-height:7px}
.logo i{display:block;width:18px;height:18px;border:2px solid var(--orange);border-radius:50%}
.menu a{position:absolute;top:25px;font-size:6px;color:#3c4b48;text-decoration:none;white-space:nowrap}
.menu a.on{color:var(--orange)}
.hero-t1{left:0;width:636px;top:101px;text-align:center;font-size:19px;font-weight:300;color:#3b4a47}
.hero-t2{left:0;width:636px;top:117px;text-align:center;font-size:36px;font-weight:800;color:var(--gold);-webkit-text-stroke:1px #c7862a;letter-spacing:.5px}
.hero-t3{left:0;width:636px;top:155px;text-align:center;font-size:16px;font-weight:300;color:var(--white)}
.hero-p{left:118px;width:400px;top:192px;text-align:center;font-size:6.5px;line-height:9px;color:var(--white)}
.btn{top:230px;height:23px;border-radius:12px;font-size:6.5px;line-height:23px;text-align:center;font-weight:600}
.btn-dark{left:248px;width:66px;background:#222;color:var(--white)}
.btn-light{left:318px;width:66px;background:#f4f1ec;color:#333}
.arrow{top:160px}

.sec-kicker{left:0;width:636px;top:361px;text-align:center;font-size:14px;color:#333}
.kick-line{top:369px;height:1px;width:78px;background:var(--teal)}
.sec-title{left:0;width:636px;top:375px;text-align:center;font-size:17px;font-weight:700;color:var(--teal)}
.sec-sub{left:0;width:636px;top:397px;text-align:center;font-size:8px;color:var(--orange)}
.about-photo{left:91px;top:432px;width:256px;height:167px;border-radius:10px;background:linear-gradient(135deg,#cfd3d6,#8fa6a2 55%,#2c6b60)}
.about-box{left:291px;top:448px;width:251px;height:136px;border-radius:8px;background:var(--box);padding:20px 14px;font-size:6px;line-height:8.5px;color:#7a7a7a}
.about-box p+p{margin-top:8px}

.sectors{left:5px;top:624px;width:631px;height:277px;background:var(--panel)}
.sectors-title{left:0;width:636px;top:643px;text-align:center;font-size:17px;font-weight:400;color:#222}
.card{top:786px;width:100px;height:98px;background:var(--white);border:1px solid #8ed7c7;border-radius:7px;text-align:center;padding:12px 6px 0}
.card h3{font-family:'Exo 2',sans-serif;font-size:9px;line-height:9px;font-weight:700;color:var(--orange);height:20px;display:flex;align-items:center;justify-content:center}
.card hr{width:12px;border:0;height:2px;background:var(--teal);margin:4px auto 7px}
.card p{font-size:5.3px;line-height:8.5px;color:#999}

.blog-title{left:0;width:636px;top:922px;text-align:center;font-size:17px;color:var(--teal)}
.post{top:971px;width:150px}
.post-img{width:150px;height:100px;border:1px solid var(--orange);border-radius:6px}
.post .date{margin-top:11px;font-size:5px;color:var(--orange);font-weight:600}
.post h4{margin-top:6px;font-size:7px;line-height:9px;font-weight:400;color:#222}
.post p{margin-top:10px;font-size:5px;line-height:8.5px;color:#666}
.post .more{margin-top:5px;font-size:5px;color:var(--teal)}

.press{left:69px;top:1189px;width:497px;height:63px;background:#e8e8e8}
.badge{top:1205px;height:33px;background:var(--white);border:1px solid #d8d8d8}
.dot-btn{top:1212px;width:14px;height:14px;border-radius:50%;background:var(--white);border:1px solid #ccc;font-size:7px;line-height:12px;text-align:center;color:#666}

.footer{left:0;top:1275px;width:636px;height:200px;background:var(--dark)}
.f-title{top:1294px;font-size:16px;font-weight:700;color:var(--teal)}
.field{left:70px;width:257px;border:1px solid #555;font-size:6px;color:#aaa;padding:5px 6px}
.social{top:1440px;width:13px;height:13px;background:var(--teal)}
.send{left:277px;top:1436px;width:50px;height:17px;background:var(--teal);color:var(--white);font-size:10px;line-height:17px;text-align:center}
.info{left:385px;font-size:6px;color:#bbb;display:flex;align-items:center;gap:7px}
.info svg{flex:none}
.copy{left:0;width:636px;top:1483px;text-align:center;font-size:5.5px;color:#666}
</style>
</head>
<body>
<div class="stage">
<div class="page">

  <div class="abs hero" role="img" aria-label="Gloved hands preparing a vaccine syringe, tinted teal to amber"></div>
  <div class="abs topbar">CALL US NOW: <b>1800 555 0142</b></div>
  <div class="abs nav"></div>
  <div class="abs logo"><i></i><span>ANTIGEN<br>PRESERVATION<br>CENTER</span></div>
  <nav class="menu">
    <a class="on" style="left:239px">HOME</a>
    <a style="left:281px">ABOUT</a>
    <a style="left:325px">VACCINES</a>
    <a style="left:376px">RESEARCH</a>
    <a style="left:437px">RECENT PUBLICATIONS</a>
    <a style="left:531px">RESOURCES</a>
  </nav>
  <div class="abs h hero-t1">STABLE VIRUS</div>
  <div class="abs h hero-t2">VIRAL VECTOR</div>
  <div class="abs h hero-t3">AND VACCINE FORMULATION</div>
  <p class="abs hero-p">Lorem Ipsum is simply dummy text of the printing and typesetting industry. Lorem Ipsum has been the industry's standard dummy text ever since the 1500s, when an unknown printer took a galley ...</p>
  <div class="abs btn btn-dark">VIEW MORE...</div>
  <div class="abs btn btn-light">CONTACT US</div>
  <svg class="abs arrow" style="left:10px" width="22" height="46"><polyline points="20,2 2,23 20,44" fill="none" stroke="#fff" stroke-width="1"/></svg>
  <svg class="abs arrow" style="left:600px" width="22" height="46"><polyline points="2,2 20,23 2,44" fill="none" stroke="#fff" stroke-width="1"/></svg>

  <div class="abs kick-line" style="left:211px"></div>
  <div class="abs kick-line" style="left:347px"></div>
  <div class="abs h sec-kicker">ABOUT</div>
  <div class="abs h sec-title">ANTIGEN PRESERVATION CENTER</div>
  <div class="abs sec-sub">Research services provider to stabilize various viruses, viral vectors, and vaccines.</div>
  <div class="abs about-photo" role="img" aria-label="Single-use syringe with a teal barrel beside surgical scissors"></div>
  <div class="abs about-box">
    <p>Aenean vehicula augue non nisi pulvinar, ut porttitor nulla dapibus. Donec semper lobortis enim, vitae sodales arcu. Quisque elit leo, interdum vitae risus eu, fermentum tincidunt arcu. Maecenas ac iaculis neque. Vivamus iaculis sit amet metus sed laoreet. Pellentesque iaculis nibh ac tortor egestas bibendum. In sed odio elit.</p>
    <p>Maecenas ac nisl vitae purus placerat faucibus sit amet non ligula. Duis quis felis nisi. Pellentesque habitant morbi tristique senectus et netus et malesuada fames ac turpis egestas. Pellentesque blandit, massa ut lobortis maximus, tortor tellus pharetra lectus, ac consectetur lectus dui a nisl. Donec auctor libero a interdum gravida.</p>
  </div>

  <div class="abs sectors"></div>
  <div class="abs h sectors-title">OUR MAIN RESEARCH SECTORS</div>
  <svg class="abs" style="left:0;top:668px" width="636" height="220">
    <line x1="292" y1="7" x2="344" y2="7" stroke="#cfcfcf"/>
    <g fill="#d4922c"><rect x="313" y="6" width="2" height="2"/><rect x="317" y="6" width="2" height="2"/><rect x="321" y="6" width="2" height="2"/></g>
    <line x1="62" y1="95" x2="571" y2="95" stroke="#b9d9d1"/>
    <g fill="#14a58a"><rect x="60" y="93" width="4" height="4"/><rect x="569" y="93" width="4" height="4"/>
      <rect x="149" y="93" width="4" height="4"/><rect x="257" y="93" width="4" height="4"/><rect x="366" y="93" width="4" height="4"/><rect x="475" y="93" width="4" height="4"/></g>
    <g stroke="#b9d9d1"><line x1="151" y1="70" x2="151" y2="118"/><line x1="259" y1="70" x2="259" y2="118"/><line x1="368" y1="70" x2="368" y2="118"/><line x1="477" y1="70" x2="477" y2="118"/></g>
    <g fill="#cfeee6" stroke="#14a58a" stroke-width="1.2">
      <circle cx="151" cy="52" r="18"/><circle cx="259" cy="52" r="18"/><circle cx="368" cy="52" r="18"/><circle cx="477" cy="52" r="18"/></g>
    <g fill="none" stroke="#1d6f60" stroke-width="1">
      <ellipse cx="151" cy="53" rx="5" ry="7"/><line x1="145" y1="50" x2="141" y2="47"/><line x1="157" y1="50" x2="161" y2="47"/><line x1="145" y1="56" x2="141" y2="59"/><line x1="157" y1="56" x2="161" y2="59"/>
      <path d="M252 60 Q259 52 266 44 M252 44 Q259 52 266 60"/><line x1="255" y1="49" x2="263" y2="49"/><line x1="255" y1="55" x2="263" y2="55"/>
      <line x1="360" y1="60" x2="376" y2="44"/><rect x="363" y="48" width="12" height="5" transform="rotate(-45 369 50)"/>
      <rect x="471" y="46" width="6" height="14"/><line x1="474" y1="42" x2="474" y2="46"/><rect x="479" y="51" width="6" height="9"/></g>
  </svg>
  <div class="abs card" style="left:101px"><h3>Viruses<br>Stabilization</h3><hr><p>Curabitur suscipit, eros rutrum iaculis vestibulum, mi mi tincidunt ante, sed dignissim urna leo eget velit. Vestibulum vitae iaculis dolor.</p></div>
  <div class="abs card" style="left:209px"><h3>Viral<br>Vectors</h3><hr><p>Curabitur suscipit, eros rutrum iaculis vestibulum, mi mi tincidunt ante, sed dignissim urna leo eget velit. Vestibulum vitae iaculis dolor.</p></div>
  <div class="abs card" style="left:318px"><h3>Vaccines</h3><hr><p>Curabitur suscipit, eros rutrum iaculis vestibulum, mi mi tincidunt ante, sed dignissim urna leo eget velit. Vestibulum vitae iaculis dolor.</p></div>
  <div class="abs card" style="left:427px"><h3>Room Temperature<br>Vaccines</h3><hr><p>Curabitur suscipit, eros rutrum iaculis vestibulum, mi mi tincidunt ante, sed dignissim urna leo eget velit. Vestibulum vitae iaculis dolor.</p></div>

  <div class="abs h blog-title">BLOG</div>
  <svg class="abs" style="left:290px;top:948px" width="56" height="8"><line x1="2" y1="4" x2="54" y2="4" stroke="#cfcfcf"/><g fill="#d4922c"><rect x="23" y="3" width="2" height="2"/><rect x="27" y="3" width="2" height="2"/><rect x="31" y="3" width="2" height="2"/></g></svg>

  <article class="abs post" style="left:70px">
    <div class="post-img" role="img" aria-label="Injection being given into a forearm" style="background:linear-gradient(135deg,#3a2418,#b57a5a 55%,#e8d6c8)"></div>
    <div class="date">14 January, 2019</div>
    <h4>Maecenas bibendum, massa sollic tudin fringilla velit sed egestas frin gilla.</h4>
    <p>Curabitur suscipit, eros rutrum iaculis vestibulum, mi mi tincidunt ante, sed dignissim urna leo eget velit. Vestibulum vitae iaculis dolor.</p>
    <div class="more">READ MORE...</div>
  </article>
  <article class="abs post" style="left:243px">
    <div class="post-img" role="img" aria-label="Medic vaccinating a patient in a clinic" style="background:linear-gradient(135deg,#6f6a5a,#4e5a3c 50%,#2a2a26)"></div>
    <div class="date">14 January, 2019</div>
    <h4>Maecenas bibendum, massa sollic tudin fringilla velit sed egestas frin gilla.</h4>
    <p>Curabitur suscipit, eros rutrum iaculis vestibulum, mi mi tincidunt ante, sed dignissim urna leo eget velit. Vestibulum vitae iaculis dolor.</p>
    <div class="more">READ MORE...</div>
  </article>
  <article class="abs post" style="left:415px">
    <div class="post-img" role="img" aria-label="Illustrated hand holding a syringe on a pink background" style="background:linear-gradient(135deg,#f3a9c8,#ec8fb5 60%,#e9c49a)"></div>
    <div class="date">14 January, 2019</div>
    <h4>Maecenas bibendum, massa sollic tudin fringilla velit sed egestas frin gilla.</h4>
    <p>Curabitur suscipit, eros rutrum iaculis vestibulum, mi mi tincidunt ante, sed dignissim urna leo eget velit. Vestibulum vitae iaculis dolor.</p>
    <div class="more">READ MORE...</div>
  </article>

  <svg class="abs" style="left:52px;top:1233px" width="532" height="20"><polygon points="0,0 18,0 18,19" fill="#c9c9c9"/><polygon points="531,0 513,0 513,19" fill="#c9c9c9"/></svg>
  <div class="abs press"></div>
  <div class="abs badge" style="left:83px;width:123px"></div>
  <div class="abs badge" style="left:218px;width:51px"></div>
  <div class="abs badge" style="left:278px;width:132px"></div>
  <div class="abs badge" style="left:419px;width:132px"></div>
  <div class="abs dot-btn" style="left:63px">‹</div>
  <div class="abs dot-btn" style="left:558px">›</div>

  <div class="abs footer"></div>
  <div class="abs h f-title" style="left:70px">CONTACT US</div>
  <div class="abs field" style="top:1326px;height:19px">NAME</div>
  <div class="abs field" style="top:1353px;height:19px">EMAIL</div>
  <div class="abs field" style="top:1381px;height:49px">MESSAGE</div>
  <div class="abs social" style="left:70px"></div>
  <div class="abs social" style="left:89px"></div>
  <div class="abs social" style="left:108px"></div>
  <div class="abs social" style="left:127px"></div>
  <div class="abs send">SEND</div>

  <div class="abs h f-title" style="left:385px">REQUEST A CALL BACK</div>
  <div class="abs" style="left:385px;top:1314px;font-size:6.5px;color:#aaa">Research services provider to stabilize various...</div>
  <div class="abs" style="left:385px;top:1328px;width:17px;height:3px;background:var(--teal)"></div>
  <div class="abs info" style="top:1342px"><svg width="8" height="6"><rect x=".5" y=".5" width="7" height="5" fill="none" stroke="#14a58a"/><polyline points=".5,.5 4,3.5 7.5,.5" fill="none" stroke="#14a58a"/></svg>contact@antigenpreservation.example</div>
  <div class="abs info" style="top:1356px;font-size:9.5px;color:#fff"><svg width="8" height="10"><rect x="1.5" y=".5" width="5" height="9" rx="1" fill="none" stroke="#14a58a"/></svg>1800 555 0142</div>
  <div class="abs info" style="top:1377px"><svg width="8" height="10"><path d="M4 9.5 C1 6 1 4.5 1 3.5 A3 3 0 0 1 7 3.5 C7 4.5 7 6 4 9.5Z" fill="#14a58a"/></svg>Lorem Ipsum is simply dummy</div>

  <div class="abs copy">© 2019 Antigen Preservation Center. All Rights Reserved.</div>
</div>
</div>
</body>
</html>
```